nonprofit organization looking for sleek new design

We need a fresh new look for this nonprofit organization, Tidewater Allies for Learning and Mutual Aid, INC (TALMA, Inc.). This organization provides educational, nutritional, dental health, and specialized services to Cedar Step children, aiming to support families meeting federal income poverty guidelines. Our mission is clear: "Creating a brighter future for the children and la familia." We focus on child development, family wellness, staff growth, and community partnerships.

```html
<!DOCTYPE html>
<html lang="en">
<head>
<meta charset="utf-8">
<title>Talma — Creating a brighter future</title>
<link rel="stylesheet" href="https://fonts.googleapis.com/css2?family=Playfair+Display:wght@500;700&family=Montserrat:wght@600;700;800&family=Mulish:wght@400;600;700&display=swap">
<style>
:root{
  --orange:#ef7d0a;
  --green:#6cc57a;
  --green-deep:#4fb25f;
  --mint:#eef9f1;
  --cream:#fbf6ef;
  --ink:#1d1d1d;
  --text:#555;
  --footer:#222222;
  --white:#ffffff;
}
*{box-sizing:border-box;margin:0;padding:0}
html,body{width:1200px;height:4267px;overflow:hidden}
body{font-family:"Mulish",sans-serif;color:var(--ink);background:var(--white);position:relative}
section,header,footer{position:absolute;left:0;width:1200px}
.abs{position:absolute}
.btn{position:absolute;background:var(--orange);color:var(--white);font-family:"Montserrat",sans-serif;font-weight:700;font-size:13px;letter-spacing:.3px;display:flex;align-items:center;justify-content:center;text-transform:uppercase}
.section-title{position:absolute;left:0;width:1200px;text-align:center;font-family:"Montserrat",sans-serif;font-weight:800;font-size:31px;letter-spacing:.5px}
.rule{position:absolute;height:3px;width:42px;background:var(--orange)}
.body-copy{font-size:14.5px;line-height:22.5px;color:var(--text)}

/* header */
.site-header{top:0;height:80px;background:var(--white)}
.brand{left:130px;top:14px;font-family:"Playfair Display",serif;font-weight:700;font-size:34px;color:var(--ink)}
.nav{left:337px;top:28px;display:flex;gap:0;font-family:"Montserrat",sans-serif;font-weight:600;font-size:14px}
.nav a{color:var(--ink);text-decoration:none;margin-right:36px}
.nav a.active{color:var(--orange);border-bottom:2px solid var(--orange);padding-bottom:10px}
.call{left:830px;top:0;width:238px;height:80px;background:var(--green);border-bottom-left-radius:40px;color:var(--white)}
.call svg{position:absolute;left:20px;top:22px}
.call .lbl{position:absolute;left:64px;top:19px;font-family:"Montserrat",sans-serif;font-size:13px;font-weight:600}
.call .num{position:absolute;left:64px;top:36px;font-family:"Montserrat",sans-serif;font-size:19px;font-weight:700}

/* hero */
.hero{top:80px;height:651px;background:linear-gradient(180deg,#3a3b39 0%,#4a4a46 55%,#6b5238 78%,#8a6a47 100%)}
.hero h1{position:absolute;left:0;width:1200px;top:28px;text-align:center;font-family:"Playfair Display",serif;font-weight:500;font-size:46px;line-height:56px;color:var(--white)}
.hero .btn{left:537px;top:156px;width:126px;height:36px;font-size:13px}
.dots{left:566px;top:617px;display:flex;gap:10px}
.dots i{width:9px;height:9px;border-radius:50%;background:var(--white);display:block}
.dots i.on{background:var(--orange)}

/* services */
.services{top:731px;height:697px}
.services .section-title{top:44px}
.service-card{position:absolute;top:144px;width:270px;height:492px;background:var(--white);border-radius:0 0 60px 60px / 0 0 24px 24px;box-shadow:0 10px 14px rgba(0,0,0,.08)}
.service-card .photo{position:absolute;left:0;top:0;width:270px;height:215px;border-radius:0 0 50% 50% / 0 0 60px 60px}
.service-card .icon{position:absolute;left:95px;top:174px;width:80px;height:80px;border-radius:50%;background:var(--green);border:4px solid var(--white);display:flex;align-items:center;justify-content:center}
.service-card h3{position:absolute;top:270px;width:100%;text-align:center;font-family:"Montserrat",sans-serif;font-weight:700;font-size:18px}
.service-card p{position:absolute;top:304px;left:28px;width:214px;text-align:center;font-size:12.5px;line-height:18.5px;color:var(--text)}
.service-card .btn{left:80px;top:421px;width:112px;height:31px;font-size:12px}

/* welcome */
.welcome{top:1428px;height:448px;background:var(--cream)}
.welcome .photo{left:0;top:0;width:613px;height:448px;background:linear-gradient(180deg,#f3dcb3 0%,#e9b86c 35%,#a8723a 70%,#4b3a23 100%)}
.welcome .photo::after{content:"";position:absolute;right:0;top:0;width:140px;height:100%;background:linear-gradient(90deg,rgba(251,246,239,0),var(--cream))}
.welcome h2{left:621px;top:44px;font-family:"Montserrat",sans-serif;font-weight:800;font-size:30px}
.welcome .rule{left:621px;top:82px;width:205px;height:3px;background:var(--ink)}
.welcome p{left:621px;top:128px;width:448px}
.welcome .btn{left:621px;top:362px;width:198px;height:36px;font-size:12px}

/* stats */
.stats{top:1876px;height:176px;background:var(--green);color:var(--white)}
.stat{position:absolute;top:36px;text-align:center;font-family:"Montserrat",sans-serif}
.stat b{display:block;font-size:27px;font-weight:700}
.stat span{display:block;font-size:14.5px;font-weight:700;line-height:27px;margin-top:4px}
.divider{position:absolute;top:28px;width:1px;height:118px;background:rgba(255,255,255,.7)}

/* programs */
.programs{top:2052px;height:666px;background:var(--mint)}
.programs .section-title{top:58px}
.program{position:absolute;top:177px;width:294px}
.program .photo{width:294px;height:253px}
.program h3{margin-top:30px;font-family:"Montserrat",sans-serif;font-weight:700;font-size:17.5px;margin-left:2px}
.program p{margin-top:10px;font-size:12.5px;line-height:18.5px;color:var(--text);width:270px;margin-left:2px}
.program .btn{position:relative;margin-top:21px;width:118px;height:36px;font-size:12px}

/* give */
.give{top:2718px;height:558px;background:var(--white)}
.give h2{left:132px;top:88px;font-family:"Montserrat",sans-serif;font-weight:800;font-size:30px}
.give p{left:132px;top:188px;width:402px}
.give .btn{left:134px;top:399px;width:128px;height:37px;font-size:13px}
.give .photo{left:567px;top:49px}

/* contact */
.contact{top:3276px;height:623px;background:linear-gradient(135deg,#62bf70 0%,#6fcb7c 50%,#5cba6a 100%)}
.contact .section-title{top:48px;color:var(--white)}
.contact .rule{left:579px;top:100px}
.form{position:absolute;left:204px;top:147px;width:794px;height:425px;background:var(--white)}
.field{position:absolute;border:1px solid #3d3d6a;font-size:13px;color:#333;padding:17px 0 0 22px}
.form .btn{left:336px;top:340px;width:125px;height:53px;font-size:17px;font-family:"Mulish",sans-serif;font-weight:700;text-transform:none;border-radius:2px}

/* footer */
.site-footer{top:3899px;height:368px;background:var(--footer);color:var(--white)}
.footer-brand{left:168px;top:108px;font-family:"Playfair Display",serif;font-weight:500;font-size:66px}
.col h4{font-family:"Montserrat",sans-serif;font-weight:700;font-size:13px}
.col .line{height:2px;background:var(--white);margin-top:10px}
.col ul{list-style:none;margin-top:18px;font-size:12px;line-height:19px}
.item{position:relative;padding-left:34px;font-size:12px;line-height:15px;margin-bottom:22px}
.item .dot{position:absolute;left:0;top:2px;width:24px;height:24px;border-radius:50%;background:var(--green);display:flex;align-items:center;justify-content:center}
.footer-rule{left:126px;top:287px;width:933px;height:1px;background:#777}
.copyright{left:0;width:1200px;top:320px;text-align:center;font-size:11px}
</style>
</head>
<body>

<header class="site-header">
  <div class="abs brand">Talma</div>
  <nav class="abs nav">
    <a class="active">HOME</a><a>ABOUT US</a><a>SERVICES</a><a>BLOG</a><a>CONTACT US</a>
  </nav>
  <div class="abs call">
    <svg width="34" height="34" viewBox="0 0 24 24" fill="none" stroke="#fff" stroke-width="1.5" stroke-linecap="round" stroke-linejoin="round"><path d="M22 16.9v3a2 2 0 0 1-2.2 2 19.8 19.8 0 0 1-8.6-3.1 19.5 19.5 0 0 1-6-6A19.8 19.8 0 0 1 2.1 4.2 2 2 0 0 1 4.1 2h3a2 2 0 0 1 2 1.7c.1.9.4 1.8.7 2.7a2 2 0 0 1-.5 2.1L8 9.8a16 16 0 0 0 6 6l1.3-1.3a2 2 0 0 1 2.1-.4c.9.3 1.8.6 2.7.7a2 2 0 0 1 1.7 2z"/><path d="M15 5a5 5 0 0 1 4 4M15 1a9 9 0 0 1 8 8"/></svg>
    <div class="lbl">CALL US</div>
    <div class="num">+1 555 014 2040</div>
  </div>
</header>

<section class="hero" role="img" aria-label="Five smiling children kneeling on a wooden floor in front of a chalkboard, holding colourful goal cards">
  <h1>Creating a brighter future<br>for the children and la familia</h1>
  <div class="btn">Read More</div>
  <div class="abs dots"><i></i><i class="on"></i><i></i><i></i></div>
</section>

<section class="services">
  <h2 class="section-title">OUR SERVICES</h2>
  <div class="rule" style="left:579px;top:101px"></div>

  <article class="service-card" style="left:28px">
    <div class="photo" role="img" aria-label="Classroom of children raising their hands" style="background:linear-gradient(160deg,#7c8aa0,#c9a98a 60%,#8c6a52)"></div>
    <div class="icon"><svg width="38" height="38" viewBox="0 0 24 24" fill="none" stroke="#fff" stroke-width="1.6"><rect x="5" y="3" width="14" height="18" rx="1"/><path d="M8 8h8M8 12h8M8 16h5"/></svg></div>
    <h3>Educational</h3>
    <p>Lorem ipsum dolor sit amet, consectetur adipiscing elit, sed do eiusmod tempor incididunt ut labore et dolore magna aliqua. Ut enim ad minim veniam, quis .</p>
    <div class="btn">Read More</div>
  </article>

  <article class="service-card" style="left:321px">
    <div class="photo" role="img" aria-label="Magnifying glass over a nutrition label beside a fresh salad" style="background:linear-gradient(150deg,#e9e2d4,#c8b04a 45%,#6e8f3a 80%)"></div>
    <div class="icon"><svg width="38" height="38" viewBox="0 0 24 24" fill="none" stroke="#fff" stroke-width="1.6"><path d="M3 12h18a9 9 0 0 1-18 0z"/><path d="M12 12c0-4 2-6 5-7M9 12c0-2 1-4 3-5"/></svg></div>
    <h3>Nutritional</h3>
    <p>Lorem ipsum dolor sit amet, consectetur adipiscing elit, sed do eiusmod tempor incididunt ut labore et dolore magna aliqua. Ut enim ad minim veniam, quis .</p>
    <div class="btn">Read More</div>
  </article>

  <article class="service-card" style="left:615px">
    <div class="photo" role="img" aria-label="Dentist examining a patient's teeth" style="background:linear-gradient(160deg,#8fb4d6,#5f8fbf 50%,#d7b3a0)"></div>
    <div class="icon"><svg width="38" height="38" viewBox="0 0 24 24" fill="none" stroke="#fff" stroke-width="1.6"><path d="M7 3c-3 0-4 3-3 6l2 11c.3 1 1.7 1 2 0l1.5-5c.5-1.5 2.5-1.5 3 0L14 20c.3 1 1.7 1 2 0l2-11c1-3 0-6-3-6-1.5 0-2 1-3 1S8.5 3 7 3z"/></svg></div>
    <h3>Dental Health</h3>
    <p>Lorem ipsum dolor sit amet, consectetur adipiscing elit, sed do eiusmod tempor incididunt ut labore et dolore magna aliqua. Ut enim ad minim veniam, quis .</p>
    <div class="btn">Read More</div>
  </article>

  <article class="service-card" style="left:908px">
    <div class="photo" role="img" aria-label="Baby looking up in soft light" style="background:linear-gradient(160deg,#dcdcd8,#cbb7a6 60%,#9fa7b8)"></div>
    <div class="icon"><svg width="38" height="38" viewBox="0 0 24 24" fill="none" stroke="#fff" stroke-width="1.6"><circle cx="12" cy="8" r="3.5"/><path d="M3 12l4 6h10l4-6"/></svg></div>
    <h3>specialized Services</h3>
    <p>Lorem ipsum dolor sit amet, consectetur adipiscing elit, sed do eiusmod tempor incididunt ut labore et dolore magna aliqua. Ut enim ad minim veniam, quis .</p>
    <div class="btn">Read More</div>
  </article>
</section>

<section class="welcome">
  <div class="abs photo" role="img" aria-label="Family silhouetted at sunset swinging a child between them"></div>
  <h2 class="abs">WELCOME TO TALMA</h2>
  <div class="abs rule"></div>
  <p class="abs body-copy">Sed ut perspiciatis unde omnis iste natus error sit voluptatem accusantium doloremque laudantium, totam rem aperiam, eaque ipsa quae ab illo inventore veritatis et quasi architecto beatae vitae dicta sunt explicabo. Nemo enim ipsam voluptatem quia voluptas sit aspernatur aut odit aut fugit, sed quia consequuntur magni dolores eos qui ratione voluptatem sequi nesciunt. Neque porro quisquam est, qui dolorem ipsum quia dolor sit amet, consectetur, adipisci velit, sed quia non numquam eius modi tempora incidunt ut labore et dolore magnam.</p>
  <div class="btn">Learn More About Us</div>
</section>

<section class="stats">
  <div class="stat" style="left:88px;width:160px"><b>20+</b><span>YEARS</span></div>
  <div class="divider" style="left:254px"></div>
  <div class="stat" style="left:290px;width:220px"><b>11M+</b><span>VISITORS ANNUALLY</span></div>
  <div class="divider" style="left:549px"></div>
  <div class="stat" style="left:578px;width:200px"><b>200K+</b><span>CHARITIES RATED</span></div>
  <div class="divider" style="left:827px"></div>
  <div class="stat" style="left:868px;width:232px"><b>$200M+</b><span>DONATED VIA OUR<br>GIVING BASKET</span></div>
</section>

<section class="programs">
  <h2 class="section-title">OUR PROGRAMS</h2>
  <div class="rule" style="left:579px;top:123px"></div>

  <article class="program" style="left:131px">
    <div class="photo" role="img" aria-label="Father carrying his daughter on his shoulders in a park" style="background:linear-gradient(170deg,#5f8f3d,#9bbf5e 55%,#3f6a2c)"></div>
    <h3>Family Wellness</h3>
    <p>Lorem ipsum dolor sit amet, consectetur adipiscing elit, sed do eiusmod tempor inci didunt ut labore et dolor.</p>
    <div class="btn">Read More</div>
  </article>

  <article class="program" style="left:452px">
    <div class="photo" role="img" aria-label="Businessman climbing a staircase toward a city skyline" style="background:linear-gradient(180deg,#c8b8a8,#e6e2dd 45%,#8b8b8b)"></div>
    <h3>Staff Growth</h3>
    <p>Lorem ipsum dolor sit amet, consectetur adipiscing elit, sed do eiusmod tempor inci didunt ut labore et dolor.</p>
    <div class="btn">Read More</div>
  </article>

  <article class="program" style="left:777px">
    <div class="photo" role="img" aria-label="Group of hands stacked together in a circle" style="background:linear-gradient(160deg,#4e6d8a,#c49a72 55%,#8a6a4a)"></div>
    <h3>Community Partnerships</h3>
    <p>Lorem ipsum dolor sit amet, consectetur adipiscing elit, sed do eiusmod tempor inci didunt ut labore et dolor.</p>
    <div class="btn">Read More</div>
  </article>
</section>

<section class="give">
  <h2 class="abs">GIVE TO THE CAUSE</h2>
  <div class="rule" style="left:132px;top:144px;width:80px"></div>
  <p class="abs body-copy">Sed ut perspiciatis unde omnis iste natus error sit voluptatem accusantium doloremque laudantium, totam rem aperiam, eaque ipsa quae ab illo inventore veritatis et quasi architecto beatae vitae dicta sunt explicabo. Nemo enim ipsam voluptatem quia voluptas sit aspernatur aut odit aut fugit, sed quia consequuntur magni dolores eos qui ratione voluptatem sequi nesciunt. Neque porro quisquam est, qui dolorem ipsum.</p>
  <div class="btn">Donate Now</div>
  <svg class="abs photo" width="503" height="462" viewBox="0 0 503 462" role="img" aria-label="Hands holding a jar of coins with a small green plant growing from it">
    <defs>
      <linearGradient id="giveTone" x1="0" y1="0" x2="0" y2="1">
        <stop offset="0" stop-color="#b9d08a"/>
        <stop offset=".45" stop-color="#d8ddc0"/>
        <stop offset=".75" stop-color="#e9c7ad"/>
        <stop offset="1" stop-color="#f4eee8"/>
      </linearGradient>
    </defs>
    <path d="M170 40C240-10 330 0 390 60c60 60 120 120 108 220-10 90-90 170-200 180-110 10-230-30-280-110C-20 270 0 170 40 120 80 75 120 70 170 40z" fill="url(#giveTone)"/>
  </svg>
</section>

<section class="contact">
  <h2 class="section-title">CONTACT US</h2>
  <div class="rule"></div>
  <form class="form">
    <div class="field" style="left:41px;top:38px;width:347px;height:52px">First Name</div>
    <div class="field" style="left:409px;top:38px;width:347px;height:52px">Last Name</div>
    <div class="field" style="left:41px;top:111px;width:347px;height:52px">Email id</div>
    <div class="field" style="left:409px;top:111px;width:347px;height:52px">Phone</div>
    <div class="field" style="left:41px;top:184px;width:715px;height:130px">Message</div>
    <div class="btn">Submit</div>
  </form>
</section>

<footer class="site-footer">
  <div class="abs footer-brand">Talma</div>

  <div class="abs col" style="left:449px;top:46px;width:192px">
    <h4>CONTACT US</h4>
    <div class="line"></div>
    <div style="margin-top:26px">
      <div class="item"><span class="dot"><svg width="12" height="12" viewBox="0 0 24 24" fill="#fff"><path d="M12 2a7 7 0 0 0-7 7c0 5 7 13 7 13s7-8 7-13a7 7 0 0 0-7-7zm0 9.5A2.5 2.5 0 1 1 12 6.5a2.5 2.5 0 0 1 0 5z"/></svg></span>214 Cedar Row,<br>Portsmouth VA 23704</div>
      <div class="item"><span class="dot"><svg width="12" height="12" viewBox="0 0 24 24" fill="#fff"><path d="M6.6 10.8a15 15 0 0 0 6.6 6.6l2.2-2.2a1 1 0 0 1 1-.3 11 11 0 0 0 3.6.6 1 1 0 0 1 1 1V20a1 1 0 0 1-1 1A17 17 0 0 1 3 4a1 1 0 0 1 1-1h3.5a1 1 0 0 1 1 1c0 1.3.2 2.5.6 3.6a1 1 0 0 1-.3 1z"/></svg></span>Call Us<br>+1 555 014 2040</div>
      <div class="item"><span class="dot"><svg width="12" height="12" viewBox="0 0 24 24" fill="#fff"><path d="M3 5h18v14H3zm2 2v.5l7 4.5 7-4.5V7z"/></svg></span>E mail Us<br>hello@talma-aid.org</div>
    </div>
  </div>

  <div class="abs col" style="left:742px;top:46px;width:107px">
    <h4>MENU</h4>
    <div class="line"></div>
    <ul><li>Home</li><li>About Us</li><li>Services</li><li>Blog</li><li>Contact Us</li></ul>
  </div>

  <div class="abs col" style="left:956px;top:46px;width:108px">
    <h4>FOLLOW US</h4>
    <div class="line"></div>
    <div style="margin-top:26px">
      <div class="item" style="margin-bottom:24px"><span class="dot"></span>Like us on<br>COMMUNITY PAGE</div>
      <div class="item" style="margin-bottom:24px"><span class="dot"></span>Follow us on<br>CAREER NETWORK</div>
      <div class="item"><span class="dot"></span>Follow us on<br>PHOTO STREAM</div>
    </div>
  </div>

  <div class="abs footer-rule"></div>
  <div class="abs copyright">Copyright © 2024 All Rights Reserved</div>
</footer>

</body>
</html>
```